Brookvale Animal Hospital brochure

We have found that our current clients do not know all of the services that we offer so we want to make a hospital brochure to make our services more known. Our website has all of our services listed but we find that clients aren't looking at our website as much as we would like so we are hoping a hospital brochure can sum up our main services and maybe lead to more people visiting our website. Our hospital colors are blue and maroon and our moto is "Outstanding Medicine, Extraordinary Service." Some of the service we would like to promote more include digital x-ray, ultrasounds, echocardiograms, laser therapy and dentals. We also offer after hours emergency care but only to our current clients. You can find more services listed on our website We are in a small town so we want a personal yet professional feel.

Feel free to visit our website to get a better feel for our business https://thebrookvalepets.example/

Industry/Entity Type

Veterinary

Requirements
Must have
• 6-8 panel brochure
Nice to have
• I included some photos from around the hospital. If you feel that you can make a few work in the brochure then great but don't feel obligated to.

```html
<!DOCTYPE html>
<html lang="en">
<head>
<meta charset="utf-8">
<title>Brookvale Animal Hospital – Brochure Back Panel</title>
<link rel="stylesheet" href="https://fonts.googleapis.com/css2?family=Nunito+Sans:ital,wght@0,300;0,400;0,600;1,300;1,400&display=swap">
<style>
  :root {
    --paper: #ffffff;
    --navy: #312a70;
    --plum: #5a2355;
    --wine: #741e3c;
    --maroon: #881a22;
    --maroon-deep: #8b1920;
    --stone: #e9e6e2;
    --frame: #ece8e4;
    --muted-rose: #b36a6e;
    --bullet-line: #a8484d;
    --text: #ffffff;
    --ink-dark: #7b1c2c;
  }
  * { box-sizing: border-box; margin: 0; padding: 0; }
  html, body {
    width: 1200px; height: 1200px; overflow: hidden;
    background: var(--paper);
    font-family: "Nunito Sans", sans-serif;
    color: var(--text);
  }
  .panel {
    position: absolute; left: 229px; top: 57px;
    width: 753px; height: 1066px;
    background: linear-gradient(180deg, var(--navy) 0%, var(--plum) 25%, var(--wine) 48%, var(--maroon) 72%, var(--maroon-deep) 100%);
    overflow: hidden;
  }
  .tile {
    position: absolute; width: 107px; height: 107px;
    display: flex; align-items: center; justify-content: center; text-align: center;
  }
  .tile--outline { border: 2px solid var(--frame); }
  .tile--stone { background: var(--stone); color: var(--ink-dark); }
  .tile--white { background: var(--paper); border: 2px solid var(--frame); border-right: none; }
  .tile--maroon { border-left: 2px solid var(--frame); border-top: 2px solid var(--frame); }
  .tile--photo { border: 2px solid var(--frame); }
  .photo-exam { background: linear-gradient(135deg, #c9c6c4 0%, #8a8680 45%, #2c3550 75%, #233049 100%); }
  .photo-dog { background: linear-gradient(135deg, #f2f0ee 0%, #e6d6c2 45%, #d8c3a8 70%, #7fa6d8 100%); }
  .service {
    font-size: 11px; font-weight: 600; line-height: 14px;
    letter-spacing: 0.6px; text-transform: uppercase; padding: 0 8px;
  }

  .brand {
    position: absolute; left: 0; width: 753px; top: 664px;
    display: flex; justify-content: center; align-items: center; gap: 8px;
  }
  .brand__mark { width: 14px; height: 14px; border-radius: 50%; background: var(--stone); }
  .brand__name { font-size: 20px; font-weight: 600; color: var(--stone); letter-spacing: 0.5px; }
  .tagline {
    position: absolute; left: 0; width: 753px; top: 711px;
    text-align: center; font-size: 10px; font-style: italic; font-weight: 400;
  }

  .hours {
    position: absolute; left: 256px; width: 240px; top: 767px;
    text-align: center; font-size: 15px; line-height: 18.2px; font-weight: 300;
  }
  .hours__title { color: var(--muted-rose); font-size: 15px; font-weight: 300; margin-bottom: 1px; }
  .hours__day { font-style: italic; }

  .emergency {
    position: absolute; left: 508px; top: 743px; width: 222px;
    font-size: 10.8px; line-height: 14.4px; font-weight: 400;
  }
  .emergency__title {
    display: flex; align-items: center; gap: 7px;
    font-size: 12.5px; font-weight: 600; line-height: 16px;
  }
  .emergency__title::before {
    content: ""; width: 7px; height: 7px; background: var(--stone);
  }

  .contact-row {
    position: absolute; left: 0; width: 753px;
    display: flex; justify-content: center; align-items: center; gap: 11px;
    font-size: 17px; font-weight: 300; white-space: nowrap;
  }
  .contact-row--address { top: 944px; }
  .contact-row--reach { top: 979px; }
  .contact-row .box {
    width: 16px; height: 16px; border: 1.5px solid var(--bullet-line); flex: none;
  }
</style>
</head>
<body>
  <main class="panel">
    <div class="tile tile--outline" style="left:216px; top:304px;"><span class="service">Digital X-Ray</span></div>
    <div class="tile tile--photo photo-exam" style="left:646px; top:304px;" role="img" aria-label="Photo of a veterinary technician performing laser therapy on a cat"></div>
    <div class="tile tile--outline" style="left:433px; top:412px;"><span class="service">Ultrasound</span></div>
    <div class="tile tile--outline" style="left:540px; top:412px;"><span class="service">Echo&shy;cardiograms</span></div>
    <div class="tile tile--white" style="left:646px; top:412px;"></div>
    <div class="tile tile--stone" style="left:109px; top:520px;"><span class="service">Dentals</span></div>
    <div class="tile tile--photo photo-dog" style="left:540px; top:520px;" role="img" aria-label="Photo of a small fluffy dog held by a veterinarian in a white coat"></div>
    <div class="tile tile--maroon" style="left:646px; top:520px;"><span class="service">Laser Therapy</span></div>
    <div class="tile tile--white" style="left:646px; top:627px;"></div>

    <div class="brand">
      <span class="brand__mark"></span>
      <span class="brand__name">Brookvale Animal Hospital</span>
    </div>
    <p class="tagline">Outstanding Medicine, Extraordinary Service</p>

    <section class="hours">
      <h2 class="hours__title">Hospital Hours</h2>
      <p><span class="hours__day">Monday:</span> 8:00am – 5:00pm</p>
      <p><span class="hours__day">Tuesday:</span> 8:00am – 8:00pm</p>
      <p><span class="hours__day">Wednesday:</span> 8:00am – 5:00pm</p>
      <p><span class="hours__day">Thursday:</span> 8:00am – 6:00pm</p>
      <p><span class="hours__day">Friday:</span> 8:00am – 4:00pm</p>
      <p><span class="hours__day">Saturday:</span> 8:00am – 1:00pm</p>
      <p><span class="hours__day">Sunday:</span> Closed</p>
    </section>

    <section class="emergency">
      <h2 class="emergency__title">Emergency Care</h2>
      <p>We are networked with <em>Ridgeline Animal Hospital</em> and <em>Valley Crest Animal Hospital</em>, to provide 24 hours emergency care for our clients. We also work with 24-hour overnight facilities in Millbrook and Stonefield. Please do not hesitate to call us if your pet needs emergency treatment.</p>
    </section>

    <div class="contact-row contact-row--address">
      <span class="box"></span><span>1420 County Route 9</span>
      <span class="box"></span><span>Brookvale, Vermont, 05000</span>
      <span class="box"></span>
    </div>
    <div class="contact-row contact-row--reach">
      <span class="box"></span><span>Tel 802-555-0148</span>
      <span class="box"></span><span>Fax: 802-555-0172</span>
      <span class="box"></span><span>Email: info@thebrookvalepets.example</span>
      <span class="box"></span>
    </div>
  </main>
</body>
</html>
```